Business card design for engineering firm specializing in defense industry.

We need a professional business card design. Something simple but stands out. We are an engineering company specializing in composites in the defense industry.
Industry/Entity Type
Defense
Contact Information for Business Card
A simple black business card with the Fibrolane yellow color is what we had in mind but open for other designs.
Colors
ffc214

```html
<!DOCTYPE html>
<html lang="en">
<head>
<meta charset="utf-8">
<title>Fibrolane Business Card</title>
<link href="https://fonts.googleapis.com/css2?family=Roboto:wght@400;500;700&display=swap" rel="stylesheet">
<style>
  :root {
    --backdrop: #2c2c2c;
    --card-front: #ebebeb;
    --ink: #2a2a2a;
    --ink-soft: #474747;
    --accent: #e4a11b;
    --pattern-dark: #1f1f1f;
    --pattern-light: #9a9a9a;
  }
  * { margin: 0; padding: 0; box-sizing: border-box; }
  html, body {
    width: 1070px; height: 1200px; overflow: hidden;
    background: var(--backdrop);
    font-family: "Roboto", Arial, sans-serif;
  }
  .card-back {
    position: absolute; left: 158px; top: 118px;
    width: 772px; height: 422px;
    background: linear-gradient(100deg, var(--pattern-light) 0%, #6a6a6a 45%, var(--pattern-dark) 100%);
  }
  .card-front {
    position: absolute; left: 150px; top: 630px;
    width: 782px; height: 430px;
    background: var(--card-front);
    border-bottom: 8px solid var(--accent);
  }
  .brand {
    position: absolute; left: 72px; top: 178px;
    display: flex; align-items: center; gap: 14px;
  }
  .brand-mark { width: 26px; height: 26px; background: var(--accent); }
  .brand-name {
    font-size: 44px; font-weight: 700; color: var(--ink);
    letter-spacing: 0.5px;
  }
  .divider {
    position: absolute; left: 414px; top: 100px;
    width: 2px; height: 226px; background: var(--ink-soft);
  }
  .details { position: absolute; left: 449px; top: 96px; color: var(--ink-soft); }
  .person-name { font-size: 27px; font-weight: 500; color: var(--ink); line-height: 32px; }
  .person-role { font-size: 20px; color: var(--accent); line-height: 24px; }
  .address { margin-top: 12px; font-size: 17px; line-height: 23px; }
  .contact-list { list-style: none; margin-top: 12px; font-size: 17px; }
  .contact-list li { display: flex; align-items: center; gap: 10px; height: 23px; }
  .contact-list svg { width: 19px; height: 17px; fill: var(--ink); flex: none; }
</style>
</head>
<body>
  <div class="card-back" role="img" aria-label="Metallic silver repeating geometric pattern covering the card back"></div>

  <div class="card-front">
    <div class="brand">
      <span class="brand-mark"></span>
      <span class="brand-name">Fibrolane</span>
    </div>
    <div class="divider"></div>
    <div class="details">
      <p class="person-name">Daniel Hartley</p>
      <p class="person-role">Founder</p>
      <p class="address">1420 Alder Court<br>Anchorage, Alaska 99501</p>
      <ul class="contact-list">
        <li><svg viewBox="0 0 24 24"><path d="M6.6 10.8a15 15 0 0 0 6.6 6.6l2.2-2.2c.3-.3.7-.4 1-.2 1.1.4 2.3.6 3.6.6.6 0 1 .4 1 1V20c0 .6-.4 1-1 1A17 17 0 0 1 3 4c0-.6.4-1 1-1h3.5c.6 0 1 .4 1 1 0 1.3.2 2.5.6 3.6.1.3 0 .7-.2 1z"/></svg>555 210 4832</li>
        <li><svg viewBox="0 0 24 24"><path d="M7 1h10a2 2 0 0 1 2 2v18a2 2 0 0 1-2 2H7a2 2 0 0 1-2-2V3a2 2 0 0 1 2-2zm0 3v14h10V4zm5 15.5a1 1 0 1 0 0 2 1 1 0 0 0 0-2z"/></svg>555 317 6290</li>
        <li><svg viewBox="0 0 24 24"><path d="M6 2h10l2 2v5H6zM3 10h18a2 2 0 0 1 2 2v6h-4v4H5v-4H1v-6a2 2 0 0 1 2-2zm4 6v4h10v-4z"/></svg>555 402 7715</li>
        <li><svg viewBox="0 0 24 24"><path d="M2 5h20v14H2zm2 2v.5l8 5 8-5V7l-8 5z"/></svg>daniel@fibrolane.com</li>
        <li><svg viewBox="0 0 24 24"><path d="M12 2a10 10 0 1 0 0 20 10 10 0 0 0 0-20zm-1 17.9A8 8 0 0 1 4.1 10L9 15v1a2 2 0 0 0 2 2zm6.9-2.5A2 2 0 0 0 16 16h-1v-3a1 1 0 0 0-1-1H8v-2h2a1 1 0 0 0 1-1V7h2a2 2 0 0 0 2-2v-.4a8 8 0 0 1 2.9 12.8z"/></svg>www.fibrolane.com</li>
      </ul>
    </div>
  </div>
</body>
</html>
```